Farmers Market Banner for a Local Producer

I am looking for a design that incorporates my logo and grabs the attention of people quickly walking by. We are growers of natural and heirloom garlic, beans and herbs. Our focus is on quality, uniqueness and honesty. Some words that have been effective for us are: heirloom, pesticide - free, local, and family farm.
We would like to see the colors of the logo in the banner, but 1 additional color if needed is fine.
Updates

We have almost decided on our final version. Another few days should do it.

Target Market(s)

Primarily female aged 25-55 that is looking for a connection with the food they eat. Quality and the growing methods are most important to them and they are open to trying new varieties of food.

Industry/Entity Type

Pesticide

Requirements
Must have
• Our location ( Alder Bend, Cedar Valley ). It should measure approx 9 feet long by 12 - 18 inches wide. This is going to be attached to the market stall canopy, either on the front or inside at the back. You are best to see one of these 10 feet by 10 feet canopies first ( Quikpop or Tarvona canopies or Brimlo canopy)
Nice to have
• We like the look and feel of our logo. This should be echoed in the banner design.
Should not have
• Cartoon art is to be avoided please.

```html
<!DOCTYPE html>
<html lang="en">
<head>
<meta charset="utf-8">
<title>Fieldhollow – Farmers Market Banner</title>
<link href="https://fonts.googleapis.com/css2?family=Open+Sans:wght@400;600;800&display=swap" rel="stylesheet">
<style>
  :root {
    --lime: #b6cc3c;
    --lime-soft: #d6e48a;
    --leaf-deep: #6f9a2e;
    --teal-soft: #8fc7cf;
    --ink: #1f2320;
    --white: #ffffff;
    --paper: #ffffff;
  }
  html, body {
    margin: 0;
    padding: 0;
    overflow: hidden;
    background: var(--paper);
  }
  .banner {
    position: relative;
    width: 1200px;
    height: 200px;
    overflow: hidden;
    background: var(--paper);
    font-family: "Open Sans", Arial, sans-serif;
  }
  .foliage-top {
    position: absolute;
    left: 0;
    top: 0;
    width: 530px;
    height: 48px;
    background: linear-gradient(90deg, var(--lime-soft) 0%, #e9f0c4 45%, #dfeee9 80%, rgba(255,255,255,0) 100%);
  }
  .foliage-right {
    position: absolute;
    right: 0;
    top: 0;
    width: 115px;
    height: 200px;
    background: linear-gradient(180deg, #e4efc9 0%, #cfe6ea 50%, var(--teal-soft) 100%);
  }
  .offer-panel {
    position: absolute;
    left: 0;
    top: 44px;
    width: 487px;
    height: 156px;
    background: var(--lime);
    text-align: center;
  }
  .offer-lead {
    position: absolute;
    left: 0;
    right: 0;
    top: 16px;
    margin: 0;
    font-size: 25px;
    font-weight: 600;
    color: var(--ink);
    line-height: 30px;
  }
  .offer-products {
    position: absolute;
    left: 0;
    right: 0;
    top: 56px;
    margin: 0;
    font-size: 31px;
    font-weight: 800;
    color: var(--white);
    line-height: 43px;
    letter-spacing: 0.5px;
    text-shadow: 2px 2px 0 var(--ink);
  }
  .brand-mark {
    position: absolute;
    left: 538px;
    top: 24px;
    width: 156px;
    height: 156px;
  }
  .brand-text {
    position: absolute;
    left: 700px;
    top: 34px;
  }
  .brand-name {
    margin: 0;
    font-size: 44px;
    font-weight: 800;
    color: var(--leaf-deep);
    line-height: 48px;
    letter-spacing: -0.5px;
  }
  .brand-tagline {
    margin: 0;
    font-size: 34px;
    font-weight: 400;
    color: var(--ink);
    line-height: 42px;
  }
  .brand-location {
    margin: 12px 0 0;
    font-size: 24px;
    font-weight: 400;
    color: var(--ink);
    line-height: 30px;
  }
</style>
</head>
<body>
  <div class="banner">
    <div class="foliage-top" role="img" aria-label="Decorative illustrated leaves, vines and hanging seeds in green and teal"></div>

    <section class="offer-panel">
      <p class="offer-lead">NATURAL AND HEIRLOOM</p>
      <p class="offer-products">GARLIC, BEANS AND<br>HERBS</p>
    </section>

    <svg class="brand-mark" viewBox="0 0 156 156" aria-hidden="true">
      <circle cx="78" cy="78" r="73" fill="none" stroke="var(--lime)" stroke-width="6"/>
    </svg>
    <div class="brand-text">
      <h1 class="brand-name">FIELDHOLLOW</h1>
      <p class="brand-tagline">raised for taste</p>
      <p class="brand-location">Alder Bend, Cedar Valley</p>
    </div>

    <div class="foliage-right" role="img" aria-label="Decorative illustrated flowers and leaves in teal, blue and green"></div>
  </div>
</body>
</html>
```